The Queen Rides Again Line of Sparkling Wine & Spirits

Back info: Tara Joy Whitfield Owner 707-555-0143 1700 E. Harlowe Rd, Bldg. 2, & 3, Fairhaven Ca. 95111
Sparkling Wines & Memorabilia www.thequeenridesagain.example
Ok I have uploaded the winning design. The color that I am after is the Fushia, Raspberry, Red, Matte Satin Matalic Finish. With a 24 Karet Gold color Foil. The Bottle is on the top row and it's the 2nd Bottle in. That is the Color that I want. This is the style of font. Make sure that you put what we're advertising. Good Luck to you all. Warmest regards, Tara
Target Market(s)
21 & up UniSex
Industry/Entity Type
Sparkling Wine and Memorabilia
Contact Information for Business Card
there listed up above.....
Look and feel

```html
<!DOCTYPE html>
<html lang="en">
<head>
<meta charset="utf-8">
<title>The Queen Rides Again – Business Cards</title>
<link rel="stylesheet" href="https://fonts.googleapis.com/css2?family=Montserrat:wght@400;500;600&family=Pinyon+Script&display=swap">
<style>
  :root {
    --backdrop: #c9c9c9;
    --fuchsia: #e0178f;
    --fuchsia-deep: #a30d66;
    --raspberry: #c0127a;
    --night: #1c0712;
    --night-rose: #3a0b25;
    --gold: #f2cb4a;
    --gold-soft: #f6dd86;
  }
  * { margin: 0; padding: 0; box-sizing: border-box; }
  html, body {
    width: 1200px; height: 800px; overflow: hidden;
    background: var(--backdrop);
    font-family: "Montserrat", sans-serif;
  }
  .stage {
    width: 1200px; height: 800px;
    display: flex; align-items: center; justify-content: center; gap: 40px;
  }
  .card {
    position: relative;
    width: 540px; height: 309px;
    overflow: hidden;
    box-shadow: 0 14px 30px rgba(0,0,0,.28);
  }
  /* Contact side */
  .card--contact {
    background: linear-gradient(135deg, var(--fuchsia-deep) 0%, var(--fuchsia) 55%, var(--raspberry) 100%);
  }
  .pattern-band {
    position: absolute; top: 0; right: 0;
    width: 190px; height: 140px;
    background: linear-gradient(160deg, var(--night-rose), var(--night));
  }
  .bottle-art {
    position: absolute; right: 48px; top: 36px;
    width: 88px; height: 226px;
    border-radius: 32px 32px 14px 14px;
    background: linear-gradient(90deg, var(--fuchsia-deep), #f03aa6 50%, var(--raspberry));
    box-shadow: 0 8px 18px rgba(0,0,0,.3);
  }
  .contact {
    position: absolute; left: 36px; top: 34px;
    width: 320px;
    color: var(--gold);
  }
  .contact__name {
    font-family: "Pinyon Script", cursive;
    font-size: 34px; line-height: 1.1;
    color: var(--gold-soft);
    white-space: nowrap;
  }
  .contact__role {
    font-size: 15px; font-weight: 400; margin-top: 2px; letter-spacing: .5px;
  }
  .contact__list {
    list-style: none; margin-top: 32px;
    font-size: 13.5px; line-height: 1.5;
  }
  .contact__list li { display: flex; align-items: center; gap: 9px; white-space: nowrap; }
  .contact__list svg { width: 13px; height: 13px; flex: none; }
  .contact__address {
    margin-top: 22px; font-size: 14.5px; line-height: 1.35; font-style: normal;
  }
  /* Brand side */
  .card--brand {
    background: radial-gradient(ellipse at 55% 60%, #e8219a 0%, var(--raspberry) 60%, var(--fuchsia-deep) 100%);
    display: flex; flex-direction: column; align-items: center; justify-content: center;
    color: var(--gold);
  }
  .brand__name {
    font-size: 38px; font-weight: 600; letter-spacing: .5px;
  }
  .brand__tagline {
    margin-top: 44px;
    font-size: 15px; font-weight: 500; letter-spacing: 1.5px;
  }
</style>
</head>
<body>
<main class="stage">
  <section class="card card--contact">
    <div class="pattern-band" role="img" aria-label="Dark ornamental lattice pattern"></div>
    <div class="bottle-art" role="img" aria-label="Illustration of a pink sparkling wine bottle with gold foil neck and crest label"></div>
    <div class="contact">
      <p class="contact__name">Tara Joy Whitfield</p>
      <p class="contact__role">Owner</p>
      <ul class="contact__list">
        <li>
          <svg viewBox="0 0 16 16" aria-hidden="true"><path fill="currentColor" d="M3.5 1l2.5 3-1.5 1.7c.9 2 2.6 3.8 4.8 4.8L11 9l3 2.5-1.5 2.8C7 14 2 9 1.7 2.5z"/></svg>
          707-555-0143
        </li>
        <li>
          <svg viewBox="0 0 16 16" aria-hidden="true"><rect x="1" y="3" width="14" height="10" fill="currentColor"/><path d="M1 3l7 6 7-6" fill="none" stroke="#c0127a" stroke-width="1.4"/></svg>
          hello@thequeenridesagain.example
        </li>
        <li>
          <svg viewBox="0 0 16 16" aria-hidden="true"><g fill="none" stroke="currentColor" stroke-width="1.4"><circle cx="8" cy="8" r="6.5"/><ellipse cx="8" cy="8" rx="2.8" ry="6.5"/><path d="M1.5 8h13"/></g></svg>
          www.thequeenridesagain.example
        </li>
      </ul>
      <address class="contact__address">1700 E. Harlowe Rd<br>Bldg. 2, &amp; 3, Fairhaven Ca. 95111</address>
    </div>
  </section>

  <section class="card card--brand">
    <h1 class="brand__name">The Queen Rides Again</h1>
    <p class="brand__tagline">SPARKLING WINES &amp; MEMORABILIA</p>
  </section>
</main>
</body>
</html>
```